Property Management Company looking for a high-end business card, letterhead and envelope design.

We provide high-end / boutique property management for real estate investors or individuals looking for someone to manage their portfolio. we are looking for a cohesive high-end design for our business cards, letterhead and envelopes.

Target Market(s)

Real Estate Investors

Industry/Entity Type

Real Estate

Requirements
Must have
• business card, letterhead and envelope design - logo attached

```html
<!DOCTYPE html>
<html lang="en">
<head>
<meta charset="utf-8">
<title>Northvale Property Management – Stationery</title>
<link rel="stylesheet" href="https://fonts.googleapis.com/css2?family=Montserrat:wght@400;700&family=Open+Sans:wght@400;600&display=swap">
<style>
  :root {
    --brand-blue: #1a547d;
    --paper: #ffffff;
    --backdrop: #eceef0;
    --ink: #4a4d50;
    --ink-soft: #7b7e81;
    --on-blue: #f2f5f8;
    --shadow: 0 2px 6px rgba(0,0,0,.12);
  }
  * { box-sizing: border-box; margin: 0; padding: 0; }
  html, body { width: 1200px; height: 795px; overflow: hidden; }
  body {
    position: relative;
    background: var(--backdrop);
    font-family: "Open Sans", sans-serif;
    color: var(--ink);
  }
  .sheet { position: absolute; background: var(--paper); box-shadow: var(--shadow); overflow: hidden; }

  /* brand name lockup */
  .brand-name {
    font-family: "Montserrat", sans-serif;
    font-weight: 700;
    color: var(--brand-blue);
    letter-spacing: .18em;
    line-height: 1;
  }
  .brand-tag {
    font-family: "Montserrat", sans-serif;
    font-weight: 400;
    color: var(--brand-blue);
    letter-spacing: .22em;
    line-height: 1;
    margin-top: 3px;
  }
  .on-blue .brand-name, .on-blue .brand-tag { color: var(--on-blue); }

  .contact-list { list-style: none; }
  .contact-list li { display: flex; align-items: center; gap: 4px; line-height: 1.45; }
  .icon { width: 1em; height: 1em; fill: var(--brand-blue); flex: none; }

  .address-band {
    position: absolute; left: 0; right: 0;
    background: var(--brand-blue); color: var(--on-blue);
    display: flex; align-items: center; gap: 5px;
  }
  .address-band .icon { fill: var(--on-blue); }

  /* letterhead */
  .letterhead { left: 40px; top: 40px; width: 320px; height: 452px; }
  .letterhead .brand { position: absolute; left: 26px; top: 28px; }
  .letterhead .brand-name { font-size: 17px; }
  .letterhead .brand-tag { font-size: 6.2px; }
  .letterhead .contact-list { position: absolute; right: 24px; top: 30px; font-size: 6.5px; }
  .letter-body { position: absolute; left: 26px; right: 26px; top: 92px; font-size: 5.6px; line-height: 1.6; color: var(--ink); }
  .letter-body p { margin-bottom: 7px; }
  .letterhead .address-band { bottom: 18px; height: 16px; padding-left: 26px; font-size: 7px; }

  /* folder */
  .folder { left: 400px; top: 40px; width: 320px; height: 452px; background: var(--brand-blue); }
  .folder .brand { position: absolute; left: 0; right: 0; top: 196px; text-align: center; }
  .folder .brand-name { font-size: 30px; }
  .folder .brand-tag { font-size: 10.5px; margin-top: 6px; }

  /* business cards */
  .card { width: 300px; height: 171px; left: 770px; }
  .card-front { top: 40px; }
  .card-front .brand { position: absolute; left: 20px; top: 48px; }
  .card-front .brand-name { font-size: 17px; }
  .card-front .brand-tag { font-size: 6.2px; }
  .card-divider { position: absolute; left: 166px; top: 40px; width: 1px; height: 72px; background: var(--brand-blue); }
  .card-person { position: absolute; left: 178px; top: 40px; font-size: 7px; }
  .person-name { font-weight: 600; color: var(--brand-blue); font-size: 8px; letter-spacing: .04em; }
  .person-role { color: var(--ink-soft); margin-bottom: 5px; }
  .card-front .address-band { bottom: 14px; height: 13px; padding-left: 20px; font-size: 6.3px; }
  .card-back { top: 232px; background: var(--brand-blue); }
  .card-back .brand { position: absolute; left: 0; right: 0; top: 58px; text-align: center; }
  .card-back .brand-name { font-size: 20px; }
  .card-back .brand-tag { font-size: 7.3px; }
  .card-web { position: absolute; left: 0; right: 0; bottom: 30px; text-align: center; font-size: 7.5px; color: var(--on-blue); letter-spacing: .05em; }

  /* envelopes */
  .envelope { top: 530px; width: 520px; height: 225px; }
  .envelope-front { left: 40px; }
  .envelope-front .brand { position: absolute; left: 28px; top: 28px; }
  .envelope-front .brand-name { font-size: 20px; }
  .envelope-front .brand-tag { font-size: 7.3px; }
  .envelope-front .contact-list { position: absolute; left: 28px; top: 92px; font-size: 8.5px; }
  .envelope-front .address-band { top: 168px; height: 18px; padding-left: 28px; font-size: 8.5px; }
  .envelope-back { left: 600px; }
  .envelope-flap {
    position: absolute; left: 0; right: 0; top: 0; height: 92px;
    background: var(--brand-blue); border-radius: 0 0 10px 10px;
  }
  .envelope-flap .brand { position: absolute; left: 0; right: 0; top: 30px; text-align: center; }
  .envelope-flap .brand-name { font-size: 19px; }
  .envelope-flap .brand-tag { font-size: 7px; }
</style>
</head>
<body>

<svg width="0" height="0" style="position:absolute" aria-hidden="true">
  <symbol id="i-phone" viewBox="0 0 24 24"><path d="M6.6 10.8a15.1 15.1 0 006.6 6.6l2.2-2.2a1 1 0 011-.25 11.4 11.4 0 003.6.57 1 1 0 011 1V20a1 1 0 01-1 1A17 17 0 013 4a1 1 0 011-1h3.5a1 1 0 011 1c0 1.25.2 2.45.57 3.57a1 1 0 01-.25 1z"/></symbol>
  <symbol id="i-fax" viewBox="0 0 24 24"><path d="M6 2h12v6H6zM3 9h18a1 1 0 011 1v8h-4v4H6v-4H2v-8a1 1 0 011-1zm5 8v3h8v-3z"/></symbol>
  <symbol id="i-mail" viewBox="0 0 24 24"><path d="M2 5h20v14H2zm2 2v.5l8 5 8-5V7l-8 5z"/></symbol>
  <symbol id="i-web" viewBox="0 0 24 24"><path d="M12 2a10 10 0 100 20 10 10 0 000-20zm6.9 6h-3a15 15 0 00-1.4-3.6A8 8 0 0118.9 8zM12 4a13 13 0 011.9 4h-3.8A13 13 0 0112 4zM4.3 14a8 8 0 010-4h3.4a16 16 0 000 4zm.8 2h3a15 15 0 001.4 3.6A8 8 0 015.1 16zm3-8h-3a8 8 0 014.4-3.6A15 15 0 008.1 8zM12 20a13 13 0 01-1.9-4h3.8A13 13 0 0112 20zm2.3-6H9.7a14 14 0 010-4h4.6a14 14 0 010 4zm.2 5.6a15 15 0 001.4-3.6h3a8 8 0 01-4.4 3.6zm1.8-5.6a16 16 0 000-4h3.4a8 8 0 010 4z"/></symbol>
  <symbol id="i-pin" viewBox="0 0 24 24"><path d="M12 2a7 7 0 00-7 7c0 5 7 13 7 13s7-8 7-13a7 7 0 00-7-7zm0 9.5A2.5 2.5 0 1112 6.5a2.5 2.5 0 010 5z"/></symbol>
</svg>

<!-- Letterhead -->
<section class="sheet letterhead" aria-label="Letterhead">
  <div class="brand">
    <div class="brand-name">NORTHVALE</div>
    <div class="brand-tag">PROPERTY MANAGEMENT</div>
  </div>
  <ul class="contact-list">
    <li><svg class="icon"><use href="#i-phone"/></svg>555.014.2200</li>
    <li><svg class="icon"><use href="#i-fax"/></svg>555.014.2291</li>
    <li><svg class="icon"><use href="#i-mail"/></svg>hello@northvale.com</li>
    <li><svg class="icon"><use href="#i-web"/></svg>www.northvaleweb.com</li>
  </ul>
  <div class="letter-body">
    <p>Dear customer,</p>
    <p>Lorem ipsum dolor sit amet, consectetur adipisicing elit, sed do eiusmod tempor incididunt ut labore et dolore magna aliqua. Ut enim ad minim veniam, quis nostrud exercitation ullamco laboris nisi ut aliquip ex ea commodo consequat. Duis aute irure dolor in reprehenderit in voluptate velit esse cillum dolore eu fugiat nulla pariatur. Excepteur sint occaecat cupidatat non proident, sunt in culpa qui officia deserunt mollit anim id est laborum.</p>
    <p>Lorem ipsum dolor sit amet, consectetur adipisicing elit, sed do eiusmod tempor incididunt ut labore et dolore magna aliqua. Ut enim ad minim veniam, quis nostrud exercitation ullamco laboris nisi ut aliquip ex ea commodo consequat. Duis aute irure dolor in reprehenderit in voluptate velit esse cillum dolore eu fugiat nulla pariatur. Excepteur sint occaecat cupidatat non proident, sunt in culpa qui officia deserunt mollit anim id est laborum.</p>
    <p>Lorem ipsum dolor sit amet, consectetur adipisicing elit, sed do eiusmod tempor incididunt ut labore et dolore magna aliqua. Ut enim ad minim veniam, quis nostrud exercitation ullamco laboris nisi ut aliquip ex ea commodo consequat. Duis aute irure dolor in reprehenderit in voluptate velit esse cillum dolore eu fugiat nulla pariatur. Excepteur sint occaecat cupidatat non proident, sunt in culpa qui officia deserunt mollit anim id est laborum.</p>
    <p>Lorem ipsum dolor sit amet, consectetur adipisicing elit, sed do eiusmod tempor incididunt ut labore et dolore magna aliqua. Ut enim ad minim veniam, quis nostrud exercitation ullamco laboris nisi ut aliquip ex ea commodo consequat. Duis aute irure dolor in reprehenderit.</p>
    <p>Yours Sincerely,</p>
  </div>
  <div class="address-band"><svg class="icon"><use href="#i-pin"/></svg>48 Harbour Lane, Oakridge, ON K2P 1L4</div>
</section>

<!-- Presentation folder -->
<section class="sheet folder on-blue" aria-label="Presentation folder">
  <div class="brand">
    <div class="brand-name">NORTHVALE</div>
    <div class="brand-tag">PROPERTY MANAGEMENT</div>
  </div>
</section>

<!-- Business card, front -->
<section class="sheet card card-front" aria-label="Business card front">
  <div class="brand">
    <div class="brand-name">NORTHVALE</div>
    <div class="brand-tag">PROPERTY MANAGEMENT</div>
  </div>
  <div class="card-divider"></div>
  <div class="card-person">
    <div class="person-name">EVAN MARLOW</div>
    <div class="person-role">Managing Director</div>
    <ul class="contact-list">
      <li><svg class="icon"><use href="#i-phone"/></svg>555.014.2200</li>
      <li><svg class="icon"><use href="#i-fax"/></svg>555.014.2291</li>
      <li><svg class="icon"><use href="#i-mail"/></svg>hello@northvale.com</li>
      <li><svg class="icon"><use href="#i-web"/></svg>www.northvaleweb.com</li>
    </ul>
  </div>
  <div class="address-band"><svg class="icon"><use href="#i-pin"/></svg>48 Harbour Lane, Oakridge, ON K2P 1L4</div>
</section>

<!-- Business card, back -->
<section class="sheet card card-back on-blue" aria-label="Business card back">
  <div class="brand">
    <div class="brand-name">NORTHVALE</div>
    <div class="brand-tag">PROPERTY MANAGEMENT</div>
  </div>
  <div class="card-web">www.northvale.com</div>
</section>

<!-- Envelope, front -->
<section class="sheet envelope envelope-front" aria-label="Envelope front">
  <div class="brand">
    <div class="brand-name">NORTHVALE</div>
    <div class="brand-tag">PROPERTY MANAGEMENT</div>
  </div>
  <ul class="contact-list">
    <li><svg class="icon"><use href="#i-phone"/></svg>555.014.2200</li>
    <li><svg class="icon"><use href="#i-fax"/></svg>555.014.2291</li>
    <li><svg class="icon"><use href="#i-mail"/></svg>hello@northvale.com</li>
    <li><svg class="icon"><use href="#i-web"/></svg>www.northvaleweb.com</li>
  </ul>
  <div class="address-band"><svg class="icon"><use href="#i-pin"/></svg>48 Harbour Lane, Oakridge, ON K2P 1L4</div>
</section>

<!-- Envelope, back -->
<section class="sheet envelope envelope-back" aria-label="Envelope back">
  <div class="envelope-flap on-blue">
    <div class="brand">
      <div class="brand-name">NORTHVALE</div>
      <div class="brand-tag">PROPERTY MANAGEMENT</div>
    </div>
  </div>
</section>

</body>
</html>
```